Webdesign for an Health & Beauty Center

We need a new modern and elegant web design for the relaunch of the http://kirelta.at/ website.
The website is for a company which offer all services for a beuty center like epilation, cosmetics and more.
The new website should use big emotional background images and a modern menu.
All in all the website should give a female expression and the design should be clear and not playful.
The existing logo used be used for the new design, the base colours of the existing website could be used optionally.

Industry/Entity Type
It Company
Look and feel
Each slider illustrates characteristics of the customer's brand and the style your logo design should communicate.

```html
<!DOCTYPE html>
<html lang="en">
<head>
<meta charset="utf-8">
<title>Kirelta Health &amp; Beauty Center</title>
<link rel="stylesheet" href="https://fonts.googleapis.com/css2?family=Arimo:wght@400;700&family=Ubuntu:wght@300;400&family=Oswald:wght@400&display=swap">
<style>
:root{
  --gold:#8c7440;
  --gold-menu:#957b4a;
  --beige-btn:#c9b58a;
  --ring:#f0ebe1;
  --text:#333;
  --muted:#555;
  --line:#d9d9d9;
  --red:#c8332b;
}
*{margin:0;padding:0;box-sizing:border-box}
html,body{width:994px;height:1200px;overflow:hidden}
body{position:relative;font-family:"Arimo",Arial,sans-serif;color:var(--text);
  background:linear-gradient(180deg,#ffffff 0,#ffffff 152px,#f6efe4 420px,#f1e8da 700px,#f4efe8 1200px)}
.abs{position:absolute}
.page-column{position:absolute;left:134px;top:152px;width:728px;height:1048px;background:#fff;box-shadow:0 0 6px rgba(0,0,0,.12)}
.header{position:absolute;left:0;top:0;width:994px;height:116px;background:#fff}
.hours-title{left:142px;top:44px;font-family:"Ubuntu",sans-serif;font-size:17px;color:var(--gold)}
.hours-text{left:142px;top:76px;font-size:9.5px;color:var(--muted)}
.brand{left:412px;top:24px;width:160px;display:flex;align-items:center;gap:6px;font-family:"Ubuntu",sans-serif;font-weight:300;font-size:34px;color:var(--gold)}
.brand-dot{width:12px;height:12px;border-radius:50%;background:var(--gold)}
.phone{left:710px;top:62px;display:flex;align-items:center;gap:8px;font-size:11px;color:#777}
.nav{position:absolute;left:0;top:116px;width:994px;height:36px;background:#fff;border-top:2px solid var(--line);border-bottom:2px solid var(--line)}
.nav ul{list-style:none;position:absolute;left:166px;top:10px;display:flex}
.nav li{font-size:9px;color:#444;letter-spacing:.2px}
.dropdown{left:263px;top:156px;width:159px;z-index:5}
.dropdown div{height:32px;background:var(--gold-menu);border-bottom:1px solid #d9ccb0;color:#fff;font-size:8.5px;padding:12px 0 0 16px}
.hero{left:142px;top:172px;width:710px;height:320px;background:radial-gradient(ellipse at 40% 60%,#e7c2a8 0,#d9b49c 25%,#bfd3d8 55%,#6a9bb0 80%,#4a7f95 100%)}
.hero-badge{left:590px;top:220px;width:232px;height:232px;border-radius:50%;background:rgba(255,255,255,.88);box-shadow:0 0 0 8px rgba(255,255,255,.45);text-align:center}
.hero-badge .name{margin-top:52px;font-family:"Ubuntu",sans-serif;font-weight:300;font-size:36px;color:var(--gold)}
.hero-badge .tag{font-family:"Oswald",sans-serif;font-size:20px;color:#8e8e8e;letter-spacing:.5px}
.hero-badge p{font-size:10.5px;line-height:16px;color:#222;margin-top:6px;padding:0 36px}
.arrows{left:803px;top:463px;display:flex;gap:1px}
.arrows span{width:19px;height:19px;background:var(--red);display:flex;align-items:center;justify-content:center}
.welcome-title{left:142px;top:514px;width:710px;text-align:center;font-family:"Ubuntu",sans-serif;font-weight:400;font-size:25px;color:var(--gold)}
.welcome-text{left:170px;top:556px;width:654px;text-align:center;font-size:9.5px;line-height:17px;color:#333}
.rule{left:142px;width:710px;height:3px;border-top:1px solid var(--line);border-bottom:1px solid var(--line)}
.feature-photo{width:100px;height:100px;border-radius:50%;border:6px solid var(--ring)}
.feature-title{font-family:"Ubuntu",sans-serif;font-size:10px;color:var(--gold);line-height:15px}
.feature-text{font-size:9px;line-height:16px;color:#333;margin-top:4px}
.promo{top:786px;width:346px;height:95px;border:4px solid var(--ring)}
.promo h3{position:absolute;left:28px;top:12px;font-family:"Ubuntu",sans-serif;font-weight:400;font-size:21px;color:#555}
.promo p{position:absolute;left:28px;top:45px;font-size:9px;color:#111}
.btn{position:absolute;background:var(--beige-btn);color:#5a4a2a;font-size:7.5px;text-align:center;padding-top:6px}
.about-photo{left:142px;top:916px;width:164px;height:164px;border-radius:50%;border:11px solid var(--ring);background:radial-gradient(circle at 55% 60%,#3a3a34 0,#5b5a45 35%,#8e8f58 65%,#b7c07a 100%)}
.about-title{left:329px;top:925px;font-family:"Ubuntu",sans-serif;font-weight:400;font-size:21px;color:var(--gold)}
.about-text{left:329px;top:961px;width:500px;font-size:8.8px;line-height:16.5px;color:#333}
.footer-links{left:150px;top:1135px;font-size:9px;color:#555;word-spacing:2px}
.copyright{left:150px;top:1159px;font-size:8.5px;color:#555}
.follow{left:674px;top:1147px;font-size:9px;color:#555}
.social{top:1139px;width:26px;height:26px;border-radius:50%;border:1px solid #bbb}
</style>
</head>
<body>
<div class="page-column"></div>

<header class="header">
  <div class="abs hours-title">Our opening times:</div>
  <div class="abs hours-text">Mon - Fri: 9:00 to 7:00 p.m. Sat: 10:00 a.m. to 3:00 p.m.</div>
  <div class="abs brand"><span class="brand-dot"></span>kirelta</div>
  <div class="abs phone">
    <svg width="28" height="28" viewBox="0 0 28 28"><circle cx="14" cy="14" r="13" fill="none" stroke="#222" stroke-width="1.5"/><path d="M10 8c-2 2-1 7 3 11s8 4 9 2l-3-3-2 1c-2-1-4-3-5-5l1-2z" fill="#222"/></svg>
    Call Us : 01/555 20 37
  </div>
</header>

<nav class="nav">
  <ul>
    <li style="width:99px">UBER UNS</li>
    <li style="width:109px">LEISTUNGEN</li>
    <li style="width:91px">GALERIE</li>
    <li style="width:106px">PFLEGELINE</li>
    <li style="width:102px">ANGEBOTE</li>
    <li style="width:110px">PREISLISTEN</li>
    <li>KONTAKT</li>
  </ul>
</nav>

<div class="abs dropdown">
  <div>LASER-HAARENTFERNUNG</div>
  <div>GEGEN FETTPÖLSTERCHEN</div>
  <div>MUSKELAUFBAU</div>
  <div>MIKRO-DERMABRASION</div>
  <div>SAUERSTOFFBEHANDLUNG</div>
</div>

<div class="abs hero" role="img" aria-label="Woman with a towel on her head receiving a relaxing back massage at a spa"></div>
<div class="abs hero-badge">
  <div class="name">Kirelta</div>
  <div class="tag">HEALTH &amp; BEAUTY CENTER</div>
  <p>We offer services for a beauty center like epilation, cosmetics etc...</p>
</div>
<div class="abs arrows">
  <span><svg width="8" height="10" viewBox="0 0 8 10"><path d="M6 1 2 5l4 4" fill="none" stroke="#fff" stroke-width="1.4"/></svg></span>
  <span><svg width="8" height="10" viewBox="0 0 8 10"><path d="M2 1l4 4-4 4" fill="none" stroke="#fff" stroke-width="1.4"/></svg></span>
</div>

<h1 class="abs welcome-title">Welcome to Kirelta</h1>
<p class="abs welcome-text">Kirelta No. 1 for aesthetic skin treatments and the leading provider of high-tech aesthetic devices according to the latest scientific standards. We place not only on a really permanent result value, but also pain-free treatments.</p>
<div class="abs rule" style="top:609px"></div>

<svg class="abs" style="left:141px;top:688px" width="10" height="12" viewBox="0 0 10 12"><path d="M7 1 2 6l5 5" fill="none" stroke="#aaa" stroke-width="1.3"/></svg>
<svg class="abs" style="left:848px;top:688px" width="10" height="12" viewBox="0 0 10 12"><path d="M3 1l5 5-5 5" fill="none" stroke="#aaa" stroke-width="1.3"/></svg>

<div class="abs feature-photo" style="left:158px;top:643px;background:radial-gradient(circle at 50% 50%,#f1c6b0,#e2a892 60%,#fbeee6)" role="img" aria-label="Smooth legs after laser hair removal"></div>
<div class="abs" style="left:273px;top:656px;width:112px">
  <div class="feature-title">LUMIS IPL<br>(LASER HAIR REMOVAL)</div>
  <div class="feature-text">Each hair that bothers you, is permanently removed! laser treatments</div>
</div>

<div class="abs feature-photo" style="left:393px;top:643px;background:radial-gradient(circle at 45% 50%,#efd3c2,#d9b29d 55%,#3b3b40)" role="img" aria-label="Woman's waist for cavitation treatment"></div>
<div class="abs" style="left:508px;top:656px;width:112px">
  <div class="feature-title">CAVITATION<br>(EXTRA FLAB)</div>
  <div class="feature-text">Each hair that bothers you, is permanently removed! laser treatments</div>
</div>

<div class="abs feature-photo" style="left:622px;top:643px;background:radial-gradient(circle at 50% 50%,#f2cdb6,#d9a486 60%,#b07a55)" role="img" aria-label="Facial muscle building treatment"></div>
<div class="abs" style="left:737px;top:656px;width:112px">
  <div class="feature-title">TONEVA<br>(MUSCLE BUILDING)</div>
  <div class="feature-text">Each hair that bothers you, is permanently removed! laser treatments</div>
</div>

<div class="abs promo" style="left:142px;background:linear-gradient(90deg,#f6ece2 0,#f1dccd 45%,#d9a98c 75%,#c48f74 100%)" role="img" aria-label="Relaxed woman lying at the spa">
  <h3>Laser Lumis</h3>
  <p>Click here for view our laser lumis</p>
  <span class="btn" style="left:28px;top:71px;width:81px;height:19px">VIEW DETAILS »</span>
</div>
<div class="abs promo" style="left:506px;background:linear-gradient(90deg,#f3ece2 0,#ece2d2 45%,#7a9a3e 72%,#3f5a2c 100%)" role="img" aria-label="Stone bowl with green bath salt and a candle">
  <h3>Care Line</h3>
  <p>Click here for view our laser lumis</p>
  <span class="btn" style="left:28px;top:71px;width:81px;height:19px">VIEW DETAILS »</span>
</div>

<div class="abs about-photo" role="img" aria-label="Spa still life with bamboo, massage stones, oil bottle and candle"></div>
<h2 class="abs about-title">About Kirelta</h2>
<div class="abs about-text">
  <p>Kirelta No. 1 for aesthetic skin treatments and the leading provider of high-tech aesthetic devices according to the latest scientific standards. We place not only on a really permanent result value, but also pain-free treatments.</p>
  <p style="margin-top:16px">Skin treatments such as the Kavitaionstherapie and the thermal Peel rejuvenate the skin without surgery and gives you a fresh and youthful appearance, the cryotherapy provides a finer complexion. See for yourself!</p>
</div>
<span class="btn" style="left:328px;top:1054px;width:81px;height:19px">VIEW DETAILS »</span>

<div class="abs rule" style="top:1113px"></div>
<div class="abs footer-links">Uber UNS &nbsp; | &nbsp; Leistungen &nbsp; | &nbsp; Galerie &nbsp; | &nbsp; Pflegeline &nbsp; | &nbsp; Angebote &nbsp; | &nbsp; Preislisten &nbsp; | &nbsp; Kontakt</div>
<div class="abs copyright">© 2014 Kirelta. All rights reserved.</div>
<div class="abs follow">Follow Us :</div>
<span class="abs social" style="left:723px"></span>
<span class="abs social" style="left:755px"></span>
<span class="abs social" style="left:787px"></span>
<span class="abs social" style="left:819px"></span>
</body>
</html>
```